HarmoNest Ensemble Jubilee
Date: Sunday Oct 2, 2022
When: 2-4 p.m.
Location: Brindle9 Alehouse
413 Marlowe Ct #200, Sacramento, CA 95821
Tickets: www.Tixolvo.com
General seating: $15 for adults and $10 for students

```html
<!DOCTYPE html>
<html lang="en">
<head>
<meta charset="UTF-8">
<title>HarmoNest Ensemble Jubilee – Flyer</title>
<link href="https://fonts.googleapis.com/css2?family=Pinyon+Script&family=Cinzel:wght@400;600&family=Montserrat:wght@800&family=Varela+Round&family=Roboto:ital,wght@1,700&display=swap" rel="stylesheet">
<style>
  :root{
    --backdrop:#c4c4c4;
    --ink:#03070c;
    --ink-soft:#0b1722;
    --cyan:#2bbde9;
    --cyan-band:#0bb0d8;
    --blue:#3f78e0;
    --pale:#d9f3ff;
    --line:#2a6fa8;
    --slate:#1d2c38;
    --slate-deep:#172530;
    --label-bg:#1b2836;
  }
  *{margin:0;padding:0;box-sizing:border-box;}
  html,body{width:800px;height:1200px;overflow:hidden;background:var(--backdrop);}
  .flyer{
    position:absolute;left:10px;top:96px;width:780px;height:1008px;
    background:radial-gradient(ellipse at 60% 45%,var(--ink-soft) 0%,var(--ink) 70%);
    overflow:hidden;box-shadow:0 6px 18px rgba(0,0,0,.35);
    color:var(--pale);
  }
  .rule{position:absolute;height:1px;background:var(--line);}
  .rule--top-left{left:52px;top:73px;width:288px;}
  .rule--top-right{left:440px;top:73px;width:288px;}
  .flourish{position:absolute;border-radius:10px;background:linear-gradient(90deg,#1a5a88,#2bbde9,#1a5a88);opacity:.8;}
  .flourish--top{left:336px;top:66px;width:108px;height:14px;}
  .flourish--mid{left:340px;top:696px;width:100px;height:10px;}
  .flourish--low{left:345px;top:830px;width:90px;height:9px;opacity:.5;}
  .title-script{
    position:absolute;left:0;right:0;top:112px;text-align:center;
    font-family:'Pinyon Script',cursive;font-size:76px;line-height:1;
    color:var(--cyan);
    background:linear-gradient(90deg,#2bbde9 0%,#3f78e0 50%,#2bbde9 100%);
    -webkit-background-clip:text;background-clip:text;-webkit-text-fill-color:transparent;
  }
  .title-caps{
    position:absolute;left:0;right:0;top:222px;text-align:center;
    font-family:'Cinzel',serif;font-size:56px;letter-spacing:1px;color:var(--cyan);
  }
  .rule--under-title{left:204px;top:296px;width:380px;background:#3a57a8;}
  .event-time{
    position:absolute;left:0;right:0;top:318px;text-align:center;
    font-family:'Cinzel',serif;font-size:20px;color:#e6eef5;letter-spacing:.5px;
  }
  .singer-photo{
    position:absolute;left:185px;top:348px;width:450px;height:292px;
    background:radial-gradient(ellipse at 52% 55%,#5a2a33 0%,#1d3345 38%,rgba(6,12,18,0) 72%);
  }
  .seating-label{
    position:absolute;left:230px;top:639px;width:312px;height:40px;
    background:var(--label-bg);text-align:center;
    font-family:'Cinzel',serif;font-weight:600;font-size:29px;line-height:40px;
    color:var(--blue);letter-spacing:1px;
  }
  .price-frame{position:absolute;left:150px;top:697px;width:480px;height:138px;}
  .price{position:absolute;top:718px;width:210px;text-align:center;}
  .price--adult{left:180px;}
  .price--student{left:386px;}
  .price__amount{display:block;font-family:'Montserrat',sans-serif;font-weight:800;font-size:54px;line-height:1;color:var(--cyan);}
  .price__who{display:block;font-family:'Varela Round',sans-serif;font-size:29px;line-height:1.2;color:#f2f7fa;letter-spacing:1px;margin-top:2px;}
  .footer-art{position:absolute;left:0;top:867px;width:780px;height:141px;}
  .venue{
    position:absolute;left:0;right:0;top:874px;text-align:center;
    font-family:'Roboto',sans-serif;font-style:italic;font-weight:700;font-size:24px;line-height:31px;
    color:var(--pale);
  }
  .booking{
    position:absolute;left:0;right:0;top:963px;text-align:center;
    font-family:'Roboto',sans-serif;font-style:italic;font-weight:700;font-size:20px;color:var(--cyan);
  }
</style>
</head>
<body>
<main class="flyer">
  <div class="rule rule--top-left"></div>
  <div class="rule rule--top-right"></div>
  <div class="flourish flourish--top" role="img" aria-label="Decorative scroll flourish"></div>

  <h1 class="title-script">HarmoNest Ensemble</h1>
  <h2 class="title-caps">JUBILEE</h2>
  <div class="rule rule--under-title"></div>
  <p class="event-time">2-4 P.M. SUNDAY OCT 2, 2022</p>

  <div class="singer-photo" role="img" aria-label="Photo of a woman singing into a microphone under red and blue stage light, with faint music notes and a treble clef behind"></div>

  <div class="seating-label">GENERAL SEATING:</div>

  <svg class="price-frame" viewBox="0 0 480 138" aria-hidden="true">
    <g fill="none" stroke="#2f5fb0" stroke-width="1.5">
      <polyline points="55,1 14,69 55,137"/>
      <polyline points="425,1 466,69 425,137"/>
      <line x1="55" y1="1" x2="190" y2="1"/>
      <line x1="290" y1="1" x2="425" y2="1"/>
      <line x1="55" y1="137" x2="195" y2="137"/>
      <line x1="285" y1="137" x2="425" y2="137"/>
      <line x1="227" y1="25" x2="227" y2="115" stroke="#4a7ad0"/>
    </g>
  </svg>
  <div class="flourish flourish--mid" role="img" aria-label="Decorative scroll flourish"></div>
  <div class="flourish flourish--low" role="img" aria-label="Decorative scroll flourish"></div>

  <div class="price price--adult"><span class="price__amount">$15</span><span class="price__who">for adults</span></div>
  <div class="price price--student"><span class="price__amount">$10</span><span class="price__who">for students</span></div>

  <svg class="footer-art" viewBox="0 0 780 141" aria-hidden="true">
    <rect x="0" y="0" width="780" height="80" fill="#0bb0d8"/>
    <rect x="0" y="79" width="780" height="62" fill="#172530"/>
    <polygon points="8,21 100,21 150,79 0,79 0,60" fill="#1d2c38"/>
    <polygon points="772,21 680,21 630,79 780,79 780,60" fill="#1d2c38"/>
    <polygon points="0,79 150,79 200,141 0,141" fill="#14202a"/>
    <polygon points="780,79 630,79 580,141 780,141" fill="#14202a"/>
  </svg>
  <p class="venue">Brindle9 Alehouse 413 Marlowe Ct #200,<br>Sacramento, CA 95821</p>
  <p class="booking">For booking visit the website: www.Tixolvo.com</p>
</main>
</body>
</html>
```